Velora Aesthetica

Medical doctor providing aesthetic medicine

* Double sided card
* Logo to be on card
Other details:
* Dr. Mirela Kostvan, BSc, MBChB, CCFP
* #214-215, 27903 83 Ave, Surrey, BC, V2T 4K7
* 604-718-2943
* info@veloraclinic.ca
* www.veloraclinic.ca

Industry/Entity Type

Medical / Health & Beauty

Contact Information for Business Card

see 'Project Description'

Colors
0054AA
0677BA
7BADD7
CADEEF
E8F1F8
FFF300
FFF600
FEFA6F
FFFEC7
FFFEE8

Requirements
Must have
• Modern, high-end design

```html
<!DOCTYPE html>
<html lang="en">
<head>
<meta charset="UTF-8">
<title>Velora Aesthetica — Business Card</title>
<link rel="stylesheet" href="https://fonts.googleapis.com/css2?family=Montserrat:wght@500;600;700&family=Poppins:wght@400;500&display=swap">
<style>
  :root {
    --canvas: #2a2a2a;
    --card: #1c1d1d;
    --card-back: #181919;
    --gold: #e2b322;
    --white: #ffffff;
    --rule: #6b6b6b;
  }
  * { box-sizing: border-box; margin: 0; padding: 0; }
  html, body { width: 1200px; height: 1108px; overflow: hidden; }
  body {
    background: var(--canvas);
    display: flex;
    align-items: center;
    justify-content: center;
    gap: 60px;
  }
  .card {
    width: 420px;
    height: 640px;
    border-radius: 28px;
    background: var(--card);
    box-shadow: 0 18px 40px rgba(0,0,0,.45);
    position: relative;
    overflow: hidden;
  }
  .card--front {
    display: flex;
    flex-direction: column;
    align-items: center;
    padding-top: 150px;
    color: var(--white);
    text-align: center;
  }
  .brand-name {
    font-family: "Montserrat", sans-serif;
    font-weight: 600;
    font-size: 34px;
    letter-spacing: 0.14em;
    text-transform: uppercase;
    line-height: 1.25;
    color: var(--white);
  }
  .brand-mark {
    width: 18px; height: 18px;
    border-radius: 50%;
    background: var(--gold);
    margin-bottom: 22px;
  }
  .doctor-name {
    margin-top: 46px;
    font-family: "Montserrat", sans-serif;
    font-weight: 700;
    font-size: 22px;
    text-transform: uppercase;
    letter-spacing: 0.01em;
  }
  .doctor-credentials {
    margin-top: 4px;
    font-family: "Montserrat", sans-serif;
    font-weight: 600;
    font-size: 20px;
    color: var(--gold);
  }
  .contact-icons {
    margin-top: 12px;
    width: 290px;
    display: flex;
    align-items: center;
    gap: 10px;
  }
  .contact-icons::before, .contact-icons::after {
    content: ""; flex: 1; height: 1px; background: var(--rule);
  }
  .icon {
    width: 28px; height: 28px;
    border-radius: 5px;
    background: var(--gold);
    display: flex; align-items: center; justify-content: center;
  }
  .icon svg { width: 18px; height: 18px; }
  .contact-list {
    margin-top: 10px;
    font-family: "Poppins", sans-serif;
    font-size: 18px;
    line-height: 1.42;
    list-style: none;
  }
  .web-domain { color: var(--gold); }
  .divider {
    margin-top: 14px;
    width: 290px; height: 1px; background: var(--rule);
  }
  .address {
    margin-top: 12px;
    font-family: "Poppins", sans-serif;
    font-style: normal;
    font-size: 18px;
    line-height: 1.4;
  }
  .card--back { background: var(--card-back); }
  .back-pattern {
    position: absolute; inset: 0;
    background: linear-gradient(160deg, #202121 0%, #181919 55%, #151616 100%);
  }
  .back-brand {
    position: absolute;
    left: 0; right: 0; bottom: 190px;
    text-align: center;
    font-family: "Montserrat", sans-serif;
    font-weight: 600;
    font-size: 14px;
    letter-spacing: 0.14em;
    text-transform: uppercase;
    color: var(--gold);
  }
</style>
</head>
<body>
  <section class="card card--front" aria-label="Card front">
    <div class="brand-mark"></div>
    <h1 class="brand-name">Velora<br>Aesthetica</h1>
    <p class="doctor-name">Dr. Mirela Kostvan</p>
    <p class="doctor-credentials">BSc, MBChB, CCFP</p>
    <div class="contact-icons">
      <span class="icon" aria-label="Phone">
        <svg viewBox="0 0 24 24" fill="#fff"><path d="M6.6 10.8a15.2 15.2 0 0 0 6.6 6.6l2.2-2.2a1 1 0 0 1 1-.25 11.4 11.4 0 0 0 3.6.57 1 1 0 0 1 1 1V20a1 1 0 0 1-1 1A17 17 0 0 1 3 4a1 1 0 0 1 1-1h3.5a1 1 0 0 1 1 1c0 1.25.2 2.45.57 3.57a1 1 0 0 1-.25 1z"/></svg>
      </span>
      <span class="icon" aria-label="Email">
        <svg viewBox="0 0 24 24" fill="none" stroke="#fff" stroke-width="2"><rect x="3" y="5" width="18" height="14" rx="1"/><path d="M3 6l9 7 9-7"/></svg>
      </span>
      <span class="icon" aria-label="Website">
        <svg viewBox="0 0 24 24" fill="none" stroke="#fff" stroke-width="1.8"><circle cx="12" cy="12" r="9"/><path d="M3 12h18M12 3c2.5 2.7 2.5 15.3 0 18M12 3c-2.5 2.7-2.5 15.3 0 18"/></svg>
      </span>
    </div>
    <ul class="contact-list">
      <li>604-718-2943</li>
      <li>info@veloraclinic.ca</li>
      <li>www.<span class="web-domain">veloraclinic</span>.ca</li>
    </ul>
    <div class="divider"></div>
    <address class="address">#214-215, 27903 83 Ave<br>Surrey, BC, V2T 4K7</address>
  </section>

  <section class="card card--back" aria-label="Card back">
    <div class="back-pattern" role="img" aria-label="Faint repeating brand pattern across the dark card back"></div>
    <p class="back-brand">Velora Aesthetica</p>
  </section>
</body>
</html>
```